Criação de Papelaria Profissional para Associações, ONGs ou Comunidades
" Somos uma Associação Comercial, onde emitimos vários documentos aos nossos associados e o principal documento é o Certificado de Origem "

```html
<!DOCTYPE html>
<html lang="pt-BR">
<head>
<meta charset="utf-8">
<title>Pasta institucional – NORVALE</title>
<link rel="stylesheet" href="https://fonts.googleapis.com/css2?family=Montserrat:wght@400;500;600;700&display=swap">
<style>
  :root {
    --page-bg: #e9eaec;
    --navy: #1d3e93;
    --navy-deep: #173381;
    --navy-light: #2a4ea6;
    --navy-shade: rgba(14, 32, 96, 0.32);
    --sky: #5aa6e8;
    --white: #ffffff;
    --paper: #f4f6fa;
    --paper-tint: #dfe6f2;
    --muted: #c9d4ee;
  }
  * { box-sizing: border-box; margin: 0; padding: 0; }
  html, body {
    width: 1200px; height: 1200px; overflow: hidden;
    background: var(--page-bg);
    font-family: "Montserrat", sans-serif;
  }
  .canvas { position: relative; width: 1200px; height: 1200px; }

  .spread {
    position: absolute; left: 220px; width: 760px; height: 530px;
    display: flex; overflow: hidden;
    box-shadow: 0 10px 28px rgba(20, 30, 60, 0.18);
  }
  .spread--outside { top: 45px; }
  .spread--inside { top: 625px; }

  .panel { position: relative; width: 50%; height: 100%; overflow: hidden; }

  /* Outside cover */
  .panel--back, .panel--front {
    background: linear-gradient(160deg, var(--navy-light) 0%, var(--navy) 45%, var(--navy-deep) 100%);
  }
  .panel--back { border-right: 1px solid rgba(255,255,255,0.08); }

  .cover-shape {
    position: absolute; left: 170px; top: 60px;
    width: 430px; height: 430px; border-radius: 50%;
    background: radial-gradient(circle, var(--navy-shade) 0%, rgba(14,32,96,0.18) 70%, rgba(14,32,96,0) 100%);
    pointer-events: none; z-index: 1;
  }

  .brand {
    position: absolute; display: flex; align-items: center; gap: 10px;
    font-weight: 600; color: var(--white); letter-spacing: 0.02em;
    z-index: 2;
  }
  .brand__dot { border-radius: 50%; background: var(--sky); flex: none; }

  .panel--front .brand { top: 100px; right: 110px; font-size: 21px; }
  .panel--front .brand__dot { width: 17px; height: 17px; }

  .panel--back .brand { left: 140px; bottom: 76px; font-size: 13px; gap: 7px; }
  .panel--back .brand__dot { width: 11px; height: 11px; }

  .address {
    position: absolute; left: 140px; bottom: 28px; z-index: 2;
    font-size: 7px; line-height: 1.6; color: var(--muted); font-style: normal;
  }
  .website {
    position: absolute; right: 30px; bottom: 36px; z-index: 2;
    font-size: 7.5px; color: var(--muted); letter-spacing: 0.04em;
  }

  /* Inside */
  .panel--inside-left, .panel--inside-right { background: var(--paper); }
  .panel--inside-left { border-right: 1px solid #d4dae5; }
  .texture {
    position: absolute; inset: 0;
    background:
      radial-gradient(ellipse at 30% 20%, rgba(255,255,255,0.7) 0%, rgba(255,255,255,0) 60%),
      linear-gradient(180deg, var(--paper) 0%, var(--paper-tint) 100%);
  }
  .pocket { position: absolute; left: 0; bottom: 0; width: 100%; height: 152px; }
  .pocket svg { display: block; width: 100%; height: 100%; }
  .pocket .brand { right: 24px; bottom: 34px; font-size: 13px; gap: 7px; }
  .pocket .brand__dot { width: 11px; height: 11px; }
</style>
</head>
<body>
<main class="canvas">

  <section class="spread spread--outside" aria-label="Pasta – lado externo">
    <div class="panel panel--back">
      <div class="brand"><span class="brand__dot"></span>NORVALE</div>
      <address class="address">
        Rua das Palmeiras, 120 – Centro<br>
        Vale Norte – SC, Brasil<br>
        (00) 0000-0000
      </address>
    </div>
    <div class="panel panel--front">
      <div class="brand"><span class="brand__dot"></span>NORVALE</div>
      <span class="website">norvale.org.br</span>
    </div>
    <div class="cover-shape" role="img" aria-label="Grande forma decorativa em azul escuro translúcido atravessando a capa"></div>
  </section>

  <section class="spread spread--inside" aria-label="Pasta – lado interno">
    <div class="panel panel--inside-left">
      <div class="texture" role="img" aria-label="Padrão tipográfico claro repetido ocupando a página interna"></div>
    </div>
    <div class="panel panel--inside-right">
      <div class="texture" role="img" aria-label="Padrão tipográfico claro repetido ocupando a página interna"></div>
      <div class="pocket">
        <svg viewBox="0 0 380 152" preserveAspectRatio="none" aria-hidden="true">
          <defs>
            <linearGradient id="pocketFill" x1="0" y1="0" x2="1" y2="1">
              <stop offset="0" stop-color="#2a4ea6"/>
              <stop offset="1" stop-color="#173381"/>
            </linearGradient>
          </defs>
          <path d="M0 152 L0 70 Q0 44 36 40 Q200 20 380 0 L380 152 Z" fill="url(#pocketFill)"/>
        </svg>
        <div class="brand"><span class="brand__dot"></span>NORVALE</div>
      </div>
    </div>
  </section>

</main>
</body>
</html>
```